Hi,

I would like to have a invitation made for a party. exactly like the picture in the link below.

http://pinboardia.example/pin/730215948361027459/

However, Please change the colors into fun/ girly feeling. font can be different and size of the card should be the same

Name of the girl: RINA
What: Bachelorette Party
Where:TOLO Boat
Dubai Coral Quay Sailing Club
When:7th of February 2013

No RSVP required. (so no need to put it)

```html
<!DOCTYPE html>
<html lang="en">
<head>
<meta charset="utf-8">
<title>RINA's Bachelorette Party Invitation</title>
<link rel="stylesheet" href="https://fonts.googleapis.com/css2?family=Federo&family=Cinzel+Decorative:wght@700&family=Anton&display=swap">
<style>
  :root {
    --paper: #ffffff;
    --ink: #1c1c1c;
    --plum: #7a2f86;
    --plum-light: #a567b8;
    --frame-blue: #3b5bb5;
    --ornament-grey: #bdbdbd;
    --ornament-dark: #6f6f6f;
    --bloom-pink: #f27bb0;
    --bloom-magenta: #d93f8c;
    --bloom-orange: #f39a3c;
    --bloom-yellow: #f5d547;
    --bloom-violet: #9b7fd6;
  }
  html, body {
    margin: 0;
    padding: 0;
    width: 1200px;
    height: 539px;
    overflow: hidden;
    background: var(--paper);
  }
  .invitation {
    display: block;
    width: 1200px;
    height: 539px;
    background: var(--paper);
  }
  .headline__name {
    font-family: "Cinzel Decorative", serif;
    font-weight: 700;
    font-size: 118px;
  }
  .headline__line {
    font-family: "Federo", sans-serif;
    font-size: 58px;
    fill: var(--ink);
  }
  .headline__single {
    font-family: "Anton", sans-serif;
    font-size: 168px;
  }
  .details__label {
    font-family: "Federo", sans-serif;
    font-size: 13px;
    fill: var(--ink);
  }
  .details__value {
    font-family: "Federo", sans-serif;
    font-size: 22px;
    fill: var(--ink);
  }
</style>
</head>
<body>
<svg class="invitation" viewBox="0 0 1200 539" xmlns="http://www.w3.org/2000/svg">
  <defs>
    <linearGradient id="name-gradient" x1="0" y1="0" x2="0" y2="1">
      <stop offset="0" stop-color="var(--plum-light)"/>
      <stop offset="1" stop-color="var(--plum)"/>
    </linearGradient>
    <linearGradient id="bloom-gradient" x1="0" y1="0" x2="1" y2="0.3">
      <stop offset="0" stop-color="var(--bloom-pink)"/>
      <stop offset="0.18" stop-color="var(--bloom-orange)"/>
      <stop offset="0.34" stop-color="var(--bloom-yellow)"/>
      <stop offset="0.5" stop-color="var(--bloom-magenta)"/>
      <stop offset="0.66" stop-color="var(--bloom-violet)"/>
      <stop offset="0.82" stop-color="var(--bloom-orange)"/>
      <stop offset="1" stop-color="var(--bloom-pink)"/>
    </linearGradient>
    <linearGradient id="divider-gradient" x1="0" y1="0" x2="1" y2="0">
      <stop offset="0" stop-color="var(--ornament-grey)" stop-opacity="0"/>
      <stop offset="0.25" stop-color="var(--ornament-grey)"/>
      <stop offset="0.5" stop-color="var(--ornament-dark)"/>
      <stop offset="0.75" stop-color="var(--ornament-grey)"/>
      <stop offset="1" stop-color="var(--ornament-grey)" stop-opacity="0"/>
    </linearGradient>
  </defs>

  <!-- top frame -->
  <g class="frame frame--top">
    <line x1="62" y1="34" x2="400" y2="34" stroke="var(--plum)" stroke-width="2"/>
    <line x1="66" y1="40" x2="394" y2="40" stroke="var(--frame-blue)" stroke-width="1.5"/>
    <line x1="66" y1="40" x2="66" y2="86" stroke="var(--frame-blue)" stroke-width="1.5"/>
    <line x1="394" y1="40" x2="394" y2="86" stroke="var(--frame-blue)" stroke-width="1.5"/>
    <rect x="52" y="20" width="26" height="26" fill="var(--plum)" role="img" aria-label="corner flourish"/>
    <rect x="382" y="20" width="26" height="26" fill="var(--plum)" role="img" aria-label="corner flourish"/>
  </g>

  <!-- bottom frame -->
  <g class="frame frame--bottom">
    <line x1="62" y1="506" x2="400" y2="506" stroke="var(--plum)" stroke-width="2"/>
    <line x1="66" y1="500" x2="394" y2="500" stroke="var(--frame-blue)" stroke-width="1.5"/>
    <line x1="66" y1="460" x2="66" y2="500" stroke="var(--frame-blue)" stroke-width="1.5"/>
    <line x1="394" y1="460" x2="394" y2="500" stroke="var(--frame-blue)" stroke-width="1.5"/>
    <rect x="52" y="494" width="26" height="26" fill="var(--plum)" role="img" aria-label="corner flourish"/>
    <rect x="382" y="494" width="26" height="26" fill="var(--plum)" role="img" aria-label="corner flourish"/>
  </g>

  <!-- scroll dividers -->
  <rect class="divider" x="435" y="180" width="360" height="10" rx="5" fill="url(#divider-gradient)" role="img" aria-label="grey scroll ornament divider"/>
  <rect class="divider" x="805" y="116" width="345" height="10" rx="5" fill="url(#divider-gradient)" role="img" aria-label="grey scroll ornament divider"/>
  <rect class="divider" x="815" y="407" width="340" height="10" rx="5" fill="url(#divider-gradient)" role="img" aria-label="grey scroll ornament divider"/>

  <!-- headline -->
  <g class="headline">
    <text class="headline__name" x="60" y="210" textLength="340" lengthAdjust="spacingAndGlyphs" fill="url(#name-gradient)">RINA's</text>
    <text class="headline__line" x="66" y="270" textLength="722" lengthAdjust="spacingAndGlyphs">LAST CHANCE TO CELEBRATE BEING</text>
    <text class="headline__single" x="52" y="424" textLength="756" lengthAdjust="spacingAndGlyphs" fill="url(#bloom-gradient)">SINGLE</text>
  </g>

  <!-- details -->
  <g class="details">
    <text class="details__label" x="850" y="212">WHAT:</text>
    <text class="details__value" x="892" y="212" textLength="178" lengthAdjust="spacingAndGlyphs">BACHELORETTE PARTY</text>

    <text class="details__label" x="850" y="268">WHERE:</text>
    <text class="details__value" x="893" y="268" textLength="92" lengthAdjust="spacingAndGlyphs">TOLO BOAT</text>
    <text class="details__value" x="893" y="295" textLength="250" lengthAdjust="spacingAndGlyphs">DUBAI CORAL QUAY SAILING CLUB</text>

    <text class="details__label" x="850" y="358">WHEN:</text>
    <text class="details__value" x="888" y="358" textLength="197" lengthAdjust="spacingAndGlyphs">7TH OF FEBRUARY 2013</text>
  </g>
</svg>
</body>
</html>
```